Harvest Poster

I need a poster for a television show. The poster would be used primarily online and I want it to be rectangle to mirror 16:9 TV aspect ratio. The name of the program is “Harvest” (logo attached). “Harvest” will be a 30 minute weekly show that features interviews from all walks of life of how the transforming power of God has changed lives. I want the logo to be included on the poster, and little section left open so I can add pictures of people that will share their story for each episode. The text should also include “Bellwick tv” logo (TV station producing show), name of producer and where the show can be viewed.
Tv

```html
<!DOCTYPE html>
<html lang="en">
<head>
<meta charset="utf-8">
<title>Harvest Poster</title>
<link href="https://fonts.googleapis.com/css2?family=Exo+2:wght@200;400;700;800&display=swap" rel="stylesheet">
<style>
  :root {
    --night: #050402;
    --gold: #c9a21a;
    --gold-soft: rgba(201, 162, 26, 0.35);
    --white: #ffffff;
    --muted: rgba(255, 255, 255, 0.78);
    --accent-red: #c8161d;
    --portrait-top: #b9b3ae;
    --portrait-bottom: #e9c3cf;
  }
  * { margin: 0; padding: 0; box-sizing: border-box; }
  html, body { width: 1200px; height: 675px; overflow: hidden; background: var(--night); }
  .poster {
    position: relative;
    width: 1200px;
    height: 675px;
    overflow: hidden;
    background: var(--night);
    font-family: "Exo 2", sans-serif;
  }
  .bokeh-field {
    position: absolute;
    inset: 0;
    background:
      radial-gradient(circle at 78% 42%, var(--gold-soft) 0, transparent 30%),
      radial-gradient(circle at 30% 35%, rgba(201,162,26,0.25) 0, transparent 22%),
      radial-gradient(circle at 60% 85%, rgba(201,162,26,0.3) 0, transparent 28%),
      radial-gradient(circle at 95% 10%, rgba(201,162,26,0.25) 0, transparent 18%),
      radial-gradient(circle at 5% 60%, rgba(201,162,26,0.2) 0, transparent 20%),
      var(--night);
  }
  .show-title {
    position: absolute;
    top: 44px;
    left: 0;
    width: 1200px;
    height: 120px;
  }
  .title-letter {
    position: absolute;
    top: 0;
    width: 80px;
    margin-left: -40px;
    text-align: center;
    font-size: 62px;
    font-weight: 200;
    line-height: 62px;
    color: var(--white);
  }
  .title-letter::after {
    content: attr(data-letter);
    position: absolute;
    left: 0;
    top: 58px;
    width: 100%;
    transform: scaleY(-1);
    opacity: 0.25;
    -webkit-mask-image: linear-gradient(to top, #000 0, transparent 60%);
            mask-image: linear-gradient(to top, #000 0, transparent 60%);
  }
  .title-letter--key {
    font-weight: 800;
    text-shadow: 0 0 14px rgba(255,255,255,0.6);
  }
  .title-letter--key::after {
    color: var(--accent-red);
    opacity: 0.9;
    text-shadow: none;
  }
  .guest-portrait {
    position: absolute;
    left: 145px;
    top: 210px;
    width: 228px;
    height: 465px;
    border-radius: 90px 90px 0 0;
    background: linear-gradient(to bottom, var(--portrait-top) 0, var(--portrait-bottom) 28%, var(--portrait-bottom) 100%);
    box-shadow: 0 0 40px 12px rgba(201,162,26,0.45);
  }
  .show-credits {
    position: absolute;
    left: 760px;
    top: 500px;
    width: 376px;
    text-align: right;
    font-size: 16px;
    font-weight: 400;
    line-height: 22px;
    color: var(--muted);
  }
  .station-name {
    position: absolute;
    left: 873px;
    top: 565px;
    width: 264px;
    text-align: right;
    font-size: 46px;
    font-weight: 700;
    line-height: 60px;
    color: var(--white);
  }
</style>
</head>
<body>
  <main class="poster">
    <div class="bokeh-field" role="img" aria-label="Dark background with soft golden out-of-focus light circles"></div>

    <h1 class="show-title" aria-label="Harvest">
      <span class="title-letter" data-letter="H" style="left:103px">H</span>
      <span class="title-letter" data-letter="A" style="left:273px">A</span>
      <span class="title-letter" data-letter="R" style="left:442px">R</span>
      <span class="title-letter title-letter--key" data-letter="V" style="left:603px">V</span>
      <span class="title-letter" data-letter="E" style="left:765px">E</span>
      <span class="title-letter" data-letter="S" style="left:934px">S</span>
      <span class="title-letter" data-letter="T" style="left:1103px">T</span>
    </h1>

    <div class="guest-portrait" role="img" aria-label="Photo of a smiling grey-haired woman in a pink shirt, the episode's guest"></div>

    <p class="show-credits">Produced by Marla Quenby<br>Weekly · Watch on Bellwick tv online</p>

    <p class="station-name">Bellwick tv</p>
  </main>
</body>
</html>
```